Bright Sprouts Business Card

speech therapy business card that is fun and professional using my logo.
Updates

Wow wonderful dedigns ... 

Industry/Entity Type

Business

Contact Information for Business Card

Tessa Morvan
Brelow Certified Practising Speech Pathologist
B.Sp.Path MSPAA CPSP
ph: 0413906281
brightsproutsspeechpathology@mailbox.example
www.brightsproutsspeechpathology.example

```html
<!DOCTYPE html>
<html lang="en">
<head>
<meta charset="utf-8">
<title>Bright Sprouts Speech Pathology – Business Card</title>
<link rel="stylesheet" href="https://fonts.googleapis.com/css2?family=Andika:wght@400;700&display=swap">
<style>
  :root {
    --backdrop: #2b2b2d;
    --brand-blue: #1a6fa8;
    --brand-blue-deep: #0b4f86;
    --brand-blue-light: #2a8cc4;
    --accent-magenta: #a3275c;
    --card-white: #ffffff;
    --card-off-white: #eef3f7;
    --text-dark: #2a2a2a;
    --divider: #d4dce3;
  }
  * { box-sizing: border-box; margin: 0; padding: 0; }
  html, body { width: 1200px; height: 900px; overflow: hidden; }
  body {
    background: var(--backdrop);
    font-family: "Andika", "Trebuchet MS", sans-serif;
    position: relative;
  }
  .card {
    position: absolute;
    top: 300px;
    width: 540px;
    height: 300px;
    border-radius: 2px;
    box-shadow: 0 18px 40px rgba(0,0,0,0.55);
    overflow: hidden;
  }
  /* Front */
  .card--front {
    left: 40px;
    background: radial-gradient(ellipse at 50% 45%, var(--brand-blue-light) 0%, var(--brand-blue) 45%, var(--brand-blue-deep) 100%);
    display: flex;
    flex-direction: column;
    align-items: center;
    justify-content: center;
    gap: 16px;
  }
  .brand-dot {
    border-radius: 50%;
    background: var(--card-white);
  }
  .card--front .brand-dot { width: 74px; height: 74px; }
  .brand-name {
    color: var(--card-white);
    font-weight: 400;
    text-align: center;
    line-height: 1.05;
    font-size: 44px;
    white-space: nowrap;
  }
  /* Back */
  .card--back {
    left: 620px;
    background: linear-gradient(180deg, var(--card-white) 0%, var(--card-off-white) 100%);
  }
  .card--back .bottom-band {
    position: absolute;
    left: 0; right: 0; bottom: 0;
    height: 22px;
    background: var(--brand-blue);
  }
  .back-brand {
    position: absolute;
    left: 14px;
    top: 74px;
    width: 180px;
    display: flex;
    flex-direction: column;
    align-items: center;
    gap: 10px;
  }
  .card--back .brand-dot { width: 44px; height: 44px; background: var(--brand-blue); }
  .back-brand .brand-name {
    color: var(--brand-blue);
    font-size: 20px;
  }
  .divider {
    position: absolute;
    left: 206px;
    top: 46px;
    width: 1px;
    height: 190px;
    background: var(--divider);
  }
  .details {
    position: absolute;
    left: 224px;
    top: 56px;
    width: 302px;
  }
  .person-name {
    color: var(--brand-blue);
    font-size: 23px;
    font-weight: 400;
    margin-bottom: 6px;
    white-space: nowrap;
  }
  .person-title {
    color: var(--accent-magenta);
    font-size: 12.5px;
    line-height: 1.25;
    margin-bottom: 22px;
    white-space: nowrap;
  }
  .contact-list { list-style: none; }
  .contact-list li {
    display: flex;
    align-items: center;
    gap: 9px;
    color: var(--text-dark);
    font-size: 11.5px;
    margin-bottom: 9px;
    white-space: nowrap;
  }
  .contact-icon { width: 14px; height: 14px; flex: none; }
</style>
</head>
<body>
  <section class="card card--front" aria-label="Business card front">
    <span class="brand-dot" aria-hidden="true"></span>
    <h1 class="brand-name">Bright Sprouts<br>Speech Pathology</h1>
  </section>

  <section class="card card--back" aria-label="Business card back">
    <div class="back-brand">
      <span class="brand-dot" aria-hidden="true"></span>
      <p class="brand-name">Bright Sprouts<br>Speech Pathology</p>
    </div>
    <div class="divider"></div>
    <div class="details">
      <h2 class="person-name">Tessa Morvan Brelow</h2>
      <p class="person-title">Certified Practising Speech Pathologist<br>B.Sp.Path MSPAA CPSP</p>
      <ul class="contact-list">
        <li>
          <svg class="contact-icon" viewBox="0 0 16 16" aria-hidden="true"><path d="M4 1.5 L6.5 4.5 L5 6.5 C6 8.5 7.5 10 9.5 11 L11.5 9.5 L14.5 12 L12.5 14.5 C7 14 2 9 1.5 3.5 Z" fill="#1a6fa8"/></svg>
          <span>0413906281</span>
        </li>
        <li>
          <svg class="contact-icon" viewBox="0 0 16 16" aria-hidden="true"><rect x="1" y="3.5" width="14" height="9" rx="1" fill="#1a6fa8"/><path d="M1.5 4 L8 9 L14.5 4" fill="none" stroke="#fff" stroke-width="1.2"/></svg>
          <span>brightsproutsspeechpathology@mailbox.example</span>
        </li>
        <li>
          <svg class="contact-icon" viewBox="0 0 16 16" aria-hidden="true"><circle cx="8" cy="8" r="6.5" fill="none" stroke="#1a6fa8" stroke-width="1.3"/><ellipse cx="8" cy="8" rx="2.8" ry="6.5" fill="none" stroke="#1a6fa8" stroke-width="1.1"/><line x1="1.5" y1="8" x2="14.5" y2="8" stroke="#1a6fa8" stroke-width="1.1"/></svg>
          <span>www.brightsproutsspeechpathology.example</span>
        </li>
      </ul>
    </div>
    <div class="bottom-band"></div>
  </section>
</body>
</html>
```